Flyer-Design - Coaching & Supervision für freib. Dipl.-Psychologin - BITTE KEINE WEITEREN DESINGS
Zielgruppe
--------- An alle, die überlegen mitzumachen - ich habe gerade als ungefähren Zeitplan, dass ich mich bis Donnerstag Abend (27.01.) entscheide, damit dann am Freitag (+evtl. Wochenende) noch Zeit für das Feintuning ist. -------------------
Ich bin Diplom-Psychologin und arbeite unter anderem freiberuflich als Coach und Supervisorin. Für diese Arbeit brauche ich einen Flyer. Ich habe bereits ein Konzept mit den Inhalten erstellt und brauche dafür nun ein professionelles Layout.
Aufgabenstellung
Anbei finden Sie das Konzept 1x als ppt (inklusive ausprobierter Alternativen zu den Fotos) und 1x als pdf.
Der Flyer hat als zentrales Thema „sich verändern / sich auf den Weg machen“ sowie die Analogie, dass ein gutes Coachinggespräch wie eine Bergtour ist.
Ich habe viel Vorarbeit gemacht (Inhalte stehen, Fotos sind recherchiert…) – sehr gerne können Sie sich kreativ ausleben und was völlig Neues / alles anders machen, es wäre aber auch ok, wenn das bereits Erarbeitete einfach graphisch aufgepimpt und professionalisiert wird.
Mein Wunsch: Ich weiß, dass der Flyer sehr voll ist. Aber ich möchte bewusst relativ viel Info dort unterbringen. Deshalb wäre es gut, wenn die Grafik des Flyers eine gewisse Leichtigkeit beinhaltet, die den vielen Text eher kaschiert. Also nicht zu verschnörkelt, sondern eher schlicht, hell und das Auge entlastend. Ich wünsche mir warme Farbtöne, die einladen und nicht zu kühl-modern wirken.
Logo:
Das Logo habe ich hier auf der Seite gestaltmarkt.de entwickeln lassen und habe alle Rechte daran. Es kann bei Bedarf auch angepasst werden.
Aktuell ist das Logo in grün, da ich dadurch den Naturbezug meiner Metapher mit aufgreife und weil die gerade entstehende Homepage, aktuell auch grün als Grundfarbe hat. Allerdings werde ich die Homepage auch noch professional überarbeiten lassen. Anbei einen Screenshot wie die Startseite der Homepage im Moment so ca. aussieht.
Bilder:
Die Fotos von mir hat ein Fotograf gemacht und ich darf sie verwenden.
Die Landschaftsbilder habe ich kostenlos und lizenzfrei von Lumora Bild ( https://bild.lumora-fotos.de/de/frei ) und von Fotelix ( https://fotelix-bilder.de/de/ ) heruntergeladen.
Falls Sie andere Bilder besser fänden und diese vorschlagen wollen, dann finden Sie weitere Details zu meinen Wünschen an die Bilder im Dokument „SelmK_AusschreibungDetails“
Die Landkarte ist ein Screenshot von KartoWeltNetz. Dort steht i..

```html
<!DOCTYPE html>
<html lang="de">
<head>
<meta charset="utf-8">
<title>Selma Kranich – Coaching und Supervision</title>
<link href="https://fonts.googleapis.com/css2?family=Itim&family=Delius&display=swap" rel="stylesheet">
<style>
  :root {
    --paper: #efeeea;
    --paper-light: #f3f2ee;
    --green: #2f7d1f;
    --green-dark: #1f6a14;
    --ink: #2b2b2b;
    --ink-soft: #3d3d3d;
    --divider: #9cc08e;
    --tagline: #f4ece2;
  }
  * { margin: 0; padding: 0; box-sizing: border-box; }
  html, body { width: 1200px; height: 848px; overflow: hidden; background: var(--paper); }
  body { font-family: "Delius", sans-serif; color: var(--ink); }
  .flyer { position: relative; width: 1200px; height: 848px; }
  .panel { position: absolute; top: 0; height: 848px; width: 400px; }
  .panel--about { left: 0; background: var(--paper); }
  .panel--places { left: 400px; background: var(--paper-light); border-left: 1px solid var(--divider); border-right: 1px solid var(--divider); }
  .panel--cover { left: 800px; overflow: hidden; }

  .heading { font-family: "Itim", cursive; color: var(--green); font-weight: 400; font-size: 27px; position: absolute; text-align: center; }

  /* About panel */
  .portrait-string { position: absolute; top: 0; width: 1px; height: 44px; background: #777; }
  .portrait-frame { position: absolute; left: 94px; top: 42px; width: 214px; height: 206px; background: #fff; padding: 8px 9px 12px; box-shadow: 0 2px 6px rgba(0,0,0,.25); transform: rotate(-0.6deg); }
  .portrait-photo { width: 100%; height: 100%; background: linear-gradient(160deg, #3a3f44 0%, #6b3a2a 45%, #c9927a 70%, #2a2e35 100%); }
  .about-heading { left: 0; width: 370px; top: 288px; }
  .cred { position: absolute; left: 70px; width: 320px; font-size: 13.6px; line-height: 17px; color: var(--ink); }
  .cred-icon { position: absolute; left: -50px; top: -4px; width: 34px; height: 34px; stroke: var(--green); fill: none; stroke-width: 1.6; stroke-linecap: round; stroke-linejoin: round; }
  .cred-sub { font-size: 12.2px; line-height: 15.5px; color: var(--ink-soft); margin-top: 3px; }
  .cred-list { list-style: none; font-size: 12.2px; line-height: 15.5px; color: var(--ink-soft); margin-top: 3px; padding-left: 14px; }
  .cred-list li::before { content: "•"; margin-right: 6px; }

  /* Places panel */
  .places-heading { left: 0; width: 400px; top: 72px; }
  .place { position: absolute; left: 69px; width: 310px; font-size: 13.6px; line-height: 17.3px; color: var(--ink); }
  .place-icon { position: absolute; left: -30px; top: -2px; width: 24px; height: 24px; stroke: var(--green); fill: none; stroke-width: 1.5; stroke-linecap: round; stroke-linejoin: round; }
  .map-area { position: absolute; left: 24px; top: 378px; width: 352px; height: 214px; background: linear-gradient(135deg, #ebe7dc 0%, #e6e4dd 55%, #cfe3d4 100%); }
  .map-arrow { position: absolute; left: 140px; top: 352px; z-index: 2; }
  .contact-heading { left: 0; width: 376px; top: 622px; }
  .contact { position: absolute; left: 122px; font-size: 14px; color: var(--ink); }
  .contact-icon { position: absolute; left: -34px; top: -4px; width: 26px; height: 26px; stroke: var(--green); fill: none; stroke-width: 1.5; stroke-linecap: round; stroke-linejoin: round; }

  /* Cover panel */
  .cover-photo { position: absolute; inset: 0; background: linear-gradient(180deg, #c9dbe4 0%, #e7ece8 30%, #e9e9de 46%, #8a8a4c 56%, #6f7a36 70%, #8d8a4a 85%, #6d7533 100%); }
  .brand { position: absolute; left: 0; width: 400px; top: 78px; text-align: center; }
  .brand-circle { width: 104px; height: 104px; border: 3px solid var(--green); border-radius: 50%; margin: 0 auto; }
  .brand-name { font-family: "Itim", cursive; color: var(--green); font-size: 36px; line-height: 40px; margin-top: 8px; }
  .brand-tag { font-family: "Delius", sans-serif; color: var(--ink); font-size: 16px; letter-spacing: 1.6px; margin-top: -2px; }
  .cover-questions { position: absolute; left: 0; width: 400px; top: 267px; text-align: center; color: var(--green); font-size: 16px; line-height: 20.5px; }
  .cover-cta { display: block; margin-top: 8px; font-weight: 700; font-size: 16.5px; color: var(--green-dark); }
  .cover-tagline { position: absolute; left: 62px; top: 596px; width: 280px; transform: rotate(-8deg); color: var(--tagline); font-family: "Itim", cursive; font-size: 21px; line-height: 25px; }
</style>
</head>
<body>
<main class="flyer">

  <section class="panel panel--about">
    <span class="portrait-string" style="left:116px"></span>
    <span class="portrait-string" style="left:275px"></span>
    <div class="portrait-frame"><div class="portrait-photo" role="img" aria-label="Porträtfoto der Coachin"></div></div>

    <h2 class="heading about-heading">Über mich</h2>

    <div class="cred" style="top:360px">
      <svg class="cred-icon" viewBox="0 0 34 34"><rect x="5" y="4" width="20" height="26" rx="2"/><path d="M9 10h12M9 14h12M9 18h8"/><circle cx="25" cy="24" r="4"/></svg>
      Diplom-Psychologin, Schwerpunkte:
      <ul class="cred-list"><li>Arbeits- und Organisationspsychologie</li><li>Systemische Familienpsychologie</li></ul>
    </div>

    <div class="cred" style="top:434px">
      <svg class="cred-icon" viewBox="0 0 34 34"><circle cx="17" cy="14" r="10"/><path d="M12 14l4 4 7-8M11 22l-4 9 5-2 2 4 3-7M23 22l4 9-5-2-2 4-3-7"/></svg>
      Zertifizierte Coachingausbildung
      <div class="cred-sub">bei WEGE Institut München-Berlin e.V. - anerkannt von EGSC (European Guild of Supervision and Coaching)</div>
    </div>

    <div class="cred" style="top:508px">
      <svg class="cred-icon" viewBox="0 0 34 34"><circle cx="17" cy="14" r="10"/><path d="M12 14l4 4 7-8M11 22l-4 9 5-2 2 4 3-7M23 22l4 9-5-2-2 4-3-7"/></svg>
      Staatlich zertifizierte Entspannungspädagogin
    </div>

    <div class="cred" style="top:545px">
      <svg class="cred-icon" viewBox="0 0 34 34"><circle cx="8" cy="14" r="3"/><path d="M3 24c0-4 2-6 5-6s5 2 5 6z"/><circle cx="16" cy="24" r="2.5"/><circle cx="24" cy="24" r="2.5"/><path d="M12 32c0-3 2-4 4-4s4 1 4 4M20 32c0-3 2-4 4-4s4 1 4 4"/><rect x="16" y="4" width="16" height="12"/><path d="M19 8h10M19 12h7"/></svg>
      Kursleiterausbildung („Train the trainer“) zur Durchführung v. Gruppenleiterausbildungen
    </div>

    <div class="cred" style="top:593px">
      <svg class="cred-icon" viewBox="0 0 34 34"><path d="M2 31l10-16 5 7 5-10 10 19z"/><path d="M22 12V3l6 2-6 2"/></svg>
      Berufserfahrung in der Wirtschaft, im sozialen und im kirchlichen Bereich
      <ul class="cred-list"><li>internationaler Großkonzern</li><li>Unternehmensberatung</li><li>Entwicklungshilfe</li><li>Betriebliche Sozialberatung (EAP)</li><li>Berufliche Fortbildungszentren</li><li>Krisenintervention</li></ul>
    </div>

    <div class="cred" style="top:737px">
      <svg class="cred-icon" viewBox="0 0 34 34"><circle cx="15" cy="17" r="11"/><path d="M7 11c4 1 5 4 3 7s2 5 2 8M20 7c-2 3 1 5 4 5s3 4 1 7"/></svg>
      Internationale Erfahrung (Englisches Coaching)
      <div class="cred-sub">1,5 Jahre Philippinen + 1,5 Jahre USA</div>
    </div>
  </section>

  <section class="panel panel--places">
    <h2 class="heading places-heading">Coaching Orte</h2>

    <p class="place" style="top:130px">
      <svg class="place-icon" viewBox="0 0 24 24"><path d="M12 21s-6-7-6-11a6 6 0 0 1 12 0c0 4-6 11-6 11z"/><circle cx="12" cy="10" r="2.2"/><path d="M8 22h8"/></svg>
      Vor Ort: direkt in Ihrem beruflichen Umfeld
    </p>
    <p class="place" style="top:167px">
      <svg class="place-icon" viewBox="0 0 24 24"><path d="M5 3l4 1 1 5-2 2c1 2 3 4 5 5l2-2 5 1 1 4-2 2C11 21 3 13 3 5z"/></svg>
      digital / telefonisch
    </p>
    <p class="place" style="top:204px">
      <svg class="place-icon" viewBox="0 0 24 24"><path d="M10 22c0-6 2-11 8-15M14 10c-4 0-8-2-9-6 4 0 8 2 9 6zM13 13c2-4 5-6 9-6-1 4-4 6-9 6z"/></svg>
      In der Natur und in Bewegung: Vielen Menschen fällt es leichter zu reden, wenn sie sich bewegen. Gerne führe ich Gespräche gemeinsam unterwegs in einem Park oder in der freien Natur. Wenn wir uns bewegen, bewegt sich auch etwas in uns.
    </p>
    <p class="place" style="top:315px">
      <svg class="place-icon" viewBox="0 0 24 24"><path d="M5 12V8a3 3 0 0 1 3-3h8a3 3 0 0 1 3 3v4"/><path d="M3 12h4v3h10v-3h4v5H3zM5 17v2M19 17v2"/></svg>
      Coachingraum: im Herzen Münchens am Lindentor
    </p>

    <div class="map-area" role="img" aria-label="Stadtplanausschnitt München mit Lage des Coachingraums"></div>
    <svg class="map-arrow" width="40" height="62" viewBox="0 0 40 62" fill="none" stroke="#222" stroke-width="2" stroke-linecap="round"><path d="M32 2c6 20 2 40-22 56"/><path d="M10 58l3-10M10 58l10-2"/></svg>

    <h2 class="heading contact-heading">Kontakt</h2>
    <p class="contact" style="top:682px">
      <svg class="contact-icon" viewBox="0 0 24 24"><path d="M5 3l4 1 1 5-2 2c1 2 3 4 5 5l2-2 5 1 1 4-2 2C11 21 3 13 3 5z"/></svg>
      +49 (0)160 4821 77 03
    </p>
    <p class="contact" style="top:720px; left:127px">
      <svg class="contact-icon" viewBox="0 0 24 24"><rect x="2" y="5" width="20" height="14"/><path d="M2 5l10 8 10-8"/></svg>
      coaching@selmakranich.de
    </p>
    <p class="contact" style="top:758px">
      <svg class="contact-icon" viewBox="0 0 24 24"><circle cx="12" cy="12" r="9.5"/><path d="M2.5 12h19M12 2.5c-5 5-5 14 0 19M12 2.5c5 5 5 14 0 19M4.5 7h15M4.5 17h15"/></svg>
      www.selmakranich.de
    </p>
  </section>

  <section class="panel panel--cover">
    <div class="cover-photo" role="img" aria-label="Landschaftsfoto: grasbewachsene Hügel mit Wanderweg und hölzernem Wegweiser unter hellem Himmel"></div>

    <div class="brand">
      <div class="brand-circle"></div>
      <div class="brand-name">Selma Kranich</div>
      <div class="brand-tag">—Coaching und Supervision—</div>
    </div>

    <p class="cover-questions">
      Stehen Sie vor einer schwierigen Situation?<br>
      Wollen Sie etwas in Ihrem Leben verändern?<br>
      Sind Sie irgendwie unzufrieden?
      <strong class="cover-cta">Möchten Sie neue Wege gehen?</strong>
    </p>

    <p class="cover-tagline">Ich mache mich mit<br>Ihnen auf den Weg!</p>
  </section>

</main>
</body>
</html>
```